Brovani Brochure

Investment company brochure related to FOREX

Industry/Entity Type

Investment

Requirements
Must have
• www.brovanigroup.com
• www.kwhmarkets.com

```html
<!DOCTYPE html>
<html lang="en">
<head>
<meta charset="UTF-8">
<title>Brovani Brochure – About Us &amp; Our Services</title>
<link rel="stylesheet" href="https://fonts.googleapis.com/css2?family=Aldrich&family=Play:wght@400;700&family=Michroma&display=swap">
<style>
  :root {
    --red: #d3161d;
    --red-deep: #8f0a10;
    --red-mid: #b8121a;
    --accent: #ee2027;
    --ink: #4a4a4a;
    --paper: #ffffff;
    --paper-tint: #fdf1f2;
  }
  * { margin: 0; padding: 0; box-sizing: border-box; }
  html, body { width: 1200px; height: 800px; overflow: hidden; background: var(--paper); }
  .spread {
    position: relative; width: 1200px; height: 800px; overflow: hidden;
    font-family: "Play", sans-serif; color: var(--ink);
    background: linear-gradient(90deg, var(--paper) 0 603px, var(--paper-tint) 603px 100%);
  }

  /* ---------- left page ---------- */
  .about-hero {
    position: absolute; left: 0; top: 0; width: 603px; height: 290px;
    background: radial-gradient(ellipse at 45% 35%, #c81e24 0%, #a90f15 45%, var(--red-deep) 100%);
  }
  .about-hero::after {
    content: ""; position: absolute; left: 0; top: 0; width: 100%; height: 100%;
    background: linear-gradient(180deg, rgba(140,8,12,0) 55%, rgba(200,20,26,.6) 100%);
  }
  .page-title {
    position: absolute; font-family: "Aldrich", sans-serif; font-weight: 400;
    color: #fff; font-size: 36px; letter-spacing: 3px; line-height: 1;
  }
  .about-title { right: 642px; top: 138px; }
  .title-rule { position: absolute; height: 1px; background: #fff; }
  .about-rule { left: 0; top: 172px; width: 561px; }
  .about-lead {
    position: absolute; right: 638px; top: 200px; width: 540px; text-align: right;
    color: #fff; font-size: 24px; line-height: 27px; letter-spacing: .3px;
  }
  .about-lead .hl { color: #ff1a22; }
  .pointer { position: absolute; }

  .body-copy {
    position: absolute; font-size: 13.2px; line-height: 20.4px; color: var(--ink);
    letter-spacing: .1px;
  }
  .about-copy { left: 43px; top: 311px; width: 520px; }

  .partners-title {
    position: absolute; left: 43px; top: 508px; font-size: 17.5px; color: var(--accent);
  }
  .service-list { position: absolute; left: 45px; top: 545px; list-style: none; }
  .service-list li {
    display: flex; align-items: center; height: 30.5px;
    font-size: 15px; color: var(--accent);
  }
  .service-list svg { margin-right: 9px; }

  /* ---------- right page ---------- */
  .services-band {
    position: absolute; left: 603px; top: 0; width: 597px; height: 111px;
    background: linear-gradient(90deg, #cc1a20 0%, #a10e14 55%, var(--red-deep) 100%);
  }
  .services-title { right: 31px; top: 40px; }
  .services-rule { left: 603px; top: 71px; width: 566px; }
  .service-heading {
    position: absolute; left: 642px; font-size: 21.5px; color: var(--accent); font-weight: 400;
  }
  .service-copy { left: 642px; width: 522px; }

  /* ---------- footer ---------- */
  .footer-band {
    position: absolute; left: 0; top: 756px; width: 1200px; height: 44px;
    background: linear-gradient(90deg, var(--red-deep) 0%, #c8161d 50%, var(--red-deep) 100%);
  }
  .footer-url {
    position: absolute; top: 17px; font-family: "Michroma", sans-serif;
    font-size: 11.5px; color: #fff; letter-spacing: 1px;
  }
  .url-left { left: 9px; }
  .url-right { right: 10px; }
</style>
</head>
<body>
<main class="spread">

  <!-- left page -->
  <section class="about">
    <div class="about-hero" role="img" aria-label="Red-toned photograph of a business handshake over documents"></div>
    <h1 class="page-title about-title">About Us</h1>
    <div class="title-rule about-rule"></div>
    <p class="about-lead"><span class="hl">Heading Text</span> here Heading Text here Heading Text here Heading Text hereHeading Text</p>
    <svg class="pointer" style="left:535px;top:290px" width="26" height="13" viewBox="0 0 26 13"><polygon points="0,0 26,0 13,13" fill="#c8161d"/></svg>

    <p class="body-copy about-copy">Subtext here Subtext here Subtext here Subtext here Subtext here Subtext here Subtext here Subtext here Subtext here Subtext here Subtext here Subtext here Subtext here Subtext here Subtext here Subtext here Subtext here Subtext here Subtext here Subtext here Subtext here Subtext here Subtext here Subtext here Subtext here Subtext here Subtext here Subtext here Subtext here Subtext here Subtext here Subtext here Subtext here Subtext here Subtext here Subtext here Subtext here Subtext here Subtext here Subtext here Subtext here Subtext here Subtext here Subtext here Subtext here Subtext here Subtext here Subtext here Subtext here Subtext here Subtext here Subtext here Subtext here</p>

    <h2 class="partners-title">The services our partners provide are :</h2>
    <ul class="service-list">
      <li><svg width="8" height="10" viewBox="0 0 8 10"><polyline points="1.5,1 6,5 1.5,9" fill="none" stroke="#ee2027" stroke-width="2.2"/></svg>Foreign exchange service</li>
      <li><svg width="8" height="10" viewBox="0 0 8 10"><polyline points="1.5,1 6,5 1.5,9" fill="none" stroke="#ee2027" stroke-width="2.2"/></svg>Covering financial risks</li>
      <li><svg width="8" height="10" viewBox="0 0 8 10"><polyline points="1.5,1 6,5 1.5,9" fill="none" stroke="#ee2027" stroke-width="2.2"/></svg>Trade credit insurance</li>
      <li><svg width="8" height="10" viewBox="0 0 8 10"><polyline points="1.5,1 6,5 1.5,9" fill="none" stroke="#ee2027" stroke-width="2.2"/></svg>Bonding</li>
      <li><svg width="8" height="10" viewBox="0 0 8 10"><polyline points="1.5,1 6,5 1.5,9" fill="none" stroke="#ee2027" stroke-width="2.2"/></svg>Trade debt collections</li>
      <li><svg width="8" height="10" viewBox="0 0 8 10"><polyline points="1.5,1 6,5 1.5,9" fill="none" stroke="#ee2027" stroke-width="2.2"/></svg>Factoring</li>
    </ul>
  </section>

  <!-- right page -->
  <section class="services">
    <div class="services-band" role="img" aria-label="Red-toned photograph of a group of business people in silhouette"></div>
    <h1 class="page-title services-title">Our Services</h1>
    <div class="title-rule services-rule"></div>
    <svg class="pointer" style="left:1143px;top:111px" width="24" height="12" viewBox="0 0 24 12"><polygon points="0,0 24,0 12,12" fill="#8f0a10"/></svg>

    <h2 class="service-heading" style="top:127px">Foreign Exchange Service</h2>
    <p class="body-copy service-copy" style="top:156px">Subtext here Subtext here Subtext here Subtext here Subtext here Subtext here Subtext here Subtext here Subtext here Subtext here Subtext here Subtext here Subtext here Subtext here Subtext here Subtext here</p>

    <h2 class="service-heading" style="top:256px">Covering Financial Risks</h2>
    <p class="body-copy service-copy" style="top:285px">Subtext here Subtext here Subtext here Subtext here Subtext here Subtext here Subtext here Subtext here Subtext here Subtext here Subtext here Subtext here Subtext here Subtext here Subtext here Subtext hereSubtext here Subtext here Subtext here Subtext here Subtext here Subtext here Subtext here Subtext here Subtext here Subtext here Subtext here Subtext here Subtext here Subtext here Subtext here Subtext here Subtext here Subtext here Subtext here Subtext here Subtext here Subtext here Subtext here Subtext here Subtext here Subtext here Subtext here Subtext here</p>

    <h2 class="service-heading" style="top:486px">Trade Credit Insurance</h2>
    <p class="body-copy service-copy" style="top:516px">Subtext here Subtext here Subtext here Subtext here Subtext here Subtext here Subtext here Subtext here Subtext here Subtext here Subtext here Subtext here Subtext here Subtext here Subtext here Subtext hereSubtext here Subtext here Subtext here Subtext here Subtext here Subtext here Subtext here Subtext here Subtext here Subtext here Subtext here Subtext here Subtext here Subtext here Subtext here Subtext here Subtext here Subtext here Subtext here Subtext here Subtext here Subtext here Subtext here Subtext here Subtext here Subtext hereSubtext here Subtext here Subtext here Subtext here Subtext here Subtext here Subtext here Subtext here Subtext here Subtext here Subtext here Subtext here Subtext here Subtext here Subtext here</p>
  </section>

  <!-- footer -->
  <footer class="footer-band">
    <span class="footer-url url-left">WWW.BROVANIGROUP.COM</span>
    <span class="footer-url url-right">WWW.KWHMARKETS.COM</span>
  </footer>

</main>
</body>
</html>
```